WWW.VELTRONA.IT BUSINNES CARD

WE NEED A BUSINESS CARD . I HAVE A COMPANY IN ITALY NR 1 IN HAIR MEDICAL CARE AN HAIR REPLECEMENT . IN CARD I NEED WRITE WEB ADDRESS, MAIL , ADDRESS, TELEPHONE NUMBER , AND NAME
IN THE BACK SIDE I NEED MY DOCTOR LOGO .
MY WEB SITE IS WWW.VELTRONA.IT
Updates

Target Market(s)

CONSUMER B2C

Industry/Entity Type

Hair And Beauty

Contact Information for Business Card

I WANT A MEDICAL BUSINESS CARD.

Font styles to use
Other font styles liked:
• VERDANA

Colors
33a6d7
3176b5
85abd2
aedbee
eaf1f7
ffffff

Requirements
Must have
• I NEED MY LOGO AND LOGO OF DR VELTRONA

```html
<!DOCTYPE html>
<html lang="it">
<head>
<meta charset="utf-8">
<title>Veltrona – Biglietto da visita</title>
<link rel="stylesheet" href="https://fonts.googleapis.com/css2?family=Varela+Round&family=Open+Sans:ital,wght@0,400;0,600;1,700&family=Oswald:wght@500&display=swap">
<style>
  :root {
    --stage: #4b3b4f;
    --navy-top: #3f72a2;
    --navy-bottom: #0d3767;
    --brand-blue: #2a7ac0;
    --list-blue: #1d4f8f;
    --sky: #33a6d7;
    --paper: #ffffff;
    --paper-shade: #eaf1f7;
    --hair-dark: #5a2d17;
    --hair-tan: #e9b48c;
  }
  * { margin: 0; padding: 0; box-sizing: border-box; }
  html, body { width: 849px; height: 1200px; overflow: hidden; }
  body {
    background: var(--stage);
    font-family: "Open Sans", Verdana, sans-serif;
    position: relative;
  }
  .card {
    position: absolute;
    left: 75px;
    width: 700px;
    height: 450px;
    box-shadow: 0 6px 18px rgba(0,0,0,.35);
    overflow: hidden;
  }
  .card--front { top: 95px; background: linear-gradient(180deg, var(--navy-top), var(--navy-bottom)); color: var(--paper); }
  .card--back { top: 615px; background: linear-gradient(180deg, var(--paper) 60%, var(--paper-shade)); color: var(--brand-blue); }
  .card__frame {
    position: absolute; inset: 14px;
    border: 1.5px solid rgba(255,255,255,.9);
  }
  .brand-name {
    position: absolute;
    font-family: "Varela Round", Verdana, sans-serif;
    white-space: nowrap;
    transform: translateX(-50%);
  }
  .card--front .brand-name { left: 340px; top: 150px; font-size: 72px; line-height: 1; }
  .card--back .brand-name { left: 240px; top: 48px; font-size: 46px; line-height: 1; color: var(--brand-blue); }
  .tagline {
    position: absolute; transform: translateX(-50%);
    white-space: nowrap; letter-spacing: .3px; text-transform: uppercase;
  }
  .card--front .tagline { left: 340px; top: 246px; font-size: 19px; }
  .card--back .tagline { left: 240px; top: 110px; font-size: 13px; color: var(--list-blue); }
  .swoosh { position: absolute; }
  .card--front .swoosh { left: 120px; top: 284px; width: 440px; height: 36px; }
  .card--back .swoosh { left: 110px; top: 136px; width: 260px; height: 22px; }
  .services {
    position: absolute; left: 240px; top: 180px; transform: translateX(-50%);
    list-style: none; text-align: center; white-space: nowrap;
    font-style: italic; font-weight: 700; font-size: 16.5px; line-height: 22px;
    color: var(--list-blue); letter-spacing: .4px;
  }
  .web {
    position: absolute; transform: translateX(-50%);
    font-family: "Oswald", "Arial Narrow", sans-serif; font-weight: 500;
    letter-spacing: 4px; white-space: nowrap;
  }
  .card--front .web { left: 340px; top: 344px; font-size: 29px; line-height: 1; }
  .card--back .web { left: 243px; top: 336px; font-size: 27px; line-height: 1; color: var(--list-blue); }
  .contact {
    position: absolute; transform: translateX(-50%);
    white-space: nowrap; letter-spacing: 3px; font-size: 17px; line-height: 1;
    display: flex; align-items: center; gap: 6px;
  }
  .card--back .contact { color: var(--list-blue); font-size: 16px; }
  .contact svg { width: 16px; height: 16px; flex: none; }
  .contact .sep { width: 14px; }
  .card--front .contact--address { left: 340px; top: 378px; }
  .card--front .contact--lines { left: 340px; top: 403px; }
  .card--back .contact--address { left: 243px; top: 372px; }
  .card--back .contact--lines { left: 243px; top: 396px; }
  .doctor-mascot {
    position: absolute; left: 497px; top: 16px; width: 190px; height: 410px;
    border-radius: 90px 90px 40px 40px;
    background: linear-gradient(180deg, var(--hair-dark) 0%, #8a4a26 55%, var(--hair-tan) 100%);
    opacity: .85;
  }
</style>
</head>
<body>

  <section class="card card--front" aria-label="Fronte del biglietto">
    <div class="card__frame"></div>
    <div class="brand-name">Veltrona</div>
    <div class="tagline">Cura e reintegrazione dei capelli</div>
    <svg class="swoosh" viewBox="0 0 440 36" aria-hidden="true">
      <path d="M0 26 C120 4 200 4 260 12 C330 22 390 22 440 2 C390 30 320 34 250 22 C190 12 110 10 0 26 Z" fill="#ffffff"/>
    </svg>
    <div class="web">WWW.VELTRONA.IT</div>
    <div class="contact contact--address">
      <svg viewBox="0 0 16 16" aria-hidden="true"><path d="M8 1.5a4.5 4.5 0 0 0-4.5 4.5c0 3.4 4.5 8.5 4.5 8.5s4.5-5.1 4.5-8.5A4.5 4.5 0 0 0 8 1.5z" fill="none" stroke="currentColor" stroke-width="1.2"/><circle cx="8" cy="6" r="1.6" fill="none" stroke="currentColor" stroke-width="1.2"/></svg>
      <span>Via Lauro 14 Padova, Italy</span>
    </div>
    <div class="contact contact--lines">
      <svg viewBox="0 0 16 16" aria-hidden="true"><rect x="1.5" y="3.5" width="13" height="9" fill="none" stroke="currentColor" stroke-width="1.2"/><path d="M1.5 3.5l6.5 5 6.5-5" fill="none" stroke="currentColor" stroke-width="1.2"/></svg>
      <span>info@veltrona.it</span>
      <span class="sep"></span>
      <svg viewBox="0 0 16 16" aria-hidden="true"><rect x="4.5" y="1.5" width="7" height="13" rx="1.2" fill="none" stroke="currentColor" stroke-width="1.2"/><line x1="7" y1="12.3" x2="9" y2="12.3" stroke="currentColor" stroke-width="1.2"/></svg>
      <span>+39049001234</span>
    </div>
  </section>

  <section class="card card--back" aria-label="Retro del biglietto">
    <div class="brand-name">Veltrona</div>
    <div class="tagline">Cura e reintegrazione dei capelli</div>
    <svg class="swoosh" viewBox="0 0 260 22" aria-hidden="true">
      <path d="M0 14 C80 2 130 6 170 10 C210 14 240 10 260 2 C240 16 200 20 160 16 C120 12 70 8 0 14 Z" fill="#33a6d7"/>
    </svg>
    <ul class="services">
      <li>• consulenza • check-up • hairtest</li>
      <li>• trattamenti e prodotti tricologici</li>
      <li>• stimolazione delle cellule staminali</li>
      <li>• autotrapianto fue • fotostimolazione</li>
      <li>• ossigenoterapia • parrucche medicali</li>
      <li>• soluzione invisibili • infoltimento naturale</li>
    </ul>
    <div class="web">WWW.VELTRONA.IT</div>
    <div class="contact contact--address">
      <svg viewBox="0 0 16 16" aria-hidden="true"><path d="M8 1.5a4.5 4.5 0 0 0-4.5 4.5c0 3.4 4.5 8.5 4.5 8.5s4.5-5.1 4.5-8.5A4.5 4.5 0 0 0 8 1.5z" fill="none" stroke="currentColor" stroke-width="1.2"/><circle cx="8" cy="6" r="1.6" fill="none" stroke="currentColor" stroke-width="1.2"/></svg>
      <span>Via Lauro 14 Padova, Italy</span>
    </div>
    <div class="contact contact--lines">
      <svg viewBox="0 0 16 16" aria-hidden="true"><rect x="1.5" y="3.5" width="13" height="9" fill="none" stroke="currentColor" stroke-width="1.2"/><path d="M1.5 3.5l6.5 5 6.5-5" fill="none" stroke="currentColor" stroke-width="1.2"/></svg>
      <span>info@veltrona.it</span>
      <span class="sep"></span>
      <svg viewBox="0 0 16 16" aria-hidden="true"><rect x="4.5" y="1.5" width="7" height="13" rx="1.2" fill="none" stroke="currentColor" stroke-width="1.2"/><line x1="7" y1="12.3" x2="9" y2="12.3" stroke="currentColor" stroke-width="1.2"/></svg>
      <span>+39049001234</span>
    </div>
    <div class="doctor-mascot" role="img" aria-label="Mascotte dr. Veltrona: un capello castano in camice da medico con pollici alzati, su un'ombra ovale color pesca, con la firma verticale dr. Veltrona"></div>
  </section>

</body>
</html>
```